Product label

Create a hip label for a small line of products to be sold at a barbershop.
Updates

Reason: I'm extending the dead line to have improvements made....also since you guys all over the world, I want to accomadet for the day and time differences. Thank you for understanding

Target Market(s)

Men with facial hair....

Industry/Entity Type

Product

Colors

Designer to choose colors to be used in the design.

Requirements
Nice to have
• Nostalgic look, current vibe, easy to read . will need room for ingredients list on the label along with business details...website, no animal testing, made in the USA and shop logo..I'm not apposed to having the logo as a secondary feature on the label as well. Please as creative as you want to be....

```html
<!DOCTYPE html>
<html lang="en">
<head>
<meta charset="utf-8">
<title>The Copper Comb – Shampoo Label</title>
<link rel="stylesheet" href="https://fonts.googleapis.com/css2?family=Rye&family=Josefin+Sans:wght@400;600&family=Playfair+Display:ital,wght@1,700&display=swap">
<style>
  :root {
    --page: #ffffff;
    --amber-edge: #6e400f;
    --amber-mid: #a9641c;
    --amber-core: #d0862c;
    --ink-light: #fbf3e6;
    --moustache-tone: #f3e7d3;
  }
  * { margin: 0; padding: 0; box-sizing: border-box; }
  html, body {
    width: 711px;
    height: 1200px;
    overflow: hidden;
    background: var(--page);
  }
  .label {
    position: relative;
    width: 711px;
    height: 1200px;
    border-radius: 180px 180px 0 0;
    background: linear-gradient(90deg,
      var(--amber-edge) 0%,
      var(--amber-mid) 18%,
      var(--amber-core) 50%,
      var(--amber-mid) 82%,
      var(--amber-edge) 100%);
    overflow: hidden;
    color: var(--ink-light);
  }
  .label__frame {
    position: absolute;
    left: 0; top: 0;
    width: 711px; height: 1200px;
  }
  .brand-name {
    position: absolute;
    top: 252px;
    left: 0; width: 100%;
    text-align: center;
    font-family: "Josefin Sans", sans-serif;
    font-weight: 600;
    font-size: 44px;
    letter-spacing: 1px;
    color: var(--ink-light);
  }
  .product-title {
    position: absolute;
    top: 414px;
    left: 0; width: 100%;
    text-align: center;
    font-family: "Rye", serif;
    font-size: 66px;
    line-height: 1;
    letter-spacing: 2px;
    color: var(--ink-light);
  }
  .ingredients {
    position: absolute;
    top: 570px;
    left: 140px;
    width: 431px;
    text-align: center;
    font-family: "Josefin Sans", sans-serif;
    font-size: 15px;
    line-height: 22.5px;
    letter-spacing: 1.6px;
    text-transform: uppercase;
  }
  .ingredients__heading {
    margin-bottom: 11px;
  }
  .moustache {
    position: absolute;
    left: 212px;
    top: 950px;
    width: 288px;
    height: 96px;
    border-radius: 48px;
    background: radial-gradient(ellipse at center, var(--moustache-tone) 0%, rgba(243,231,211,0.55) 60%, rgba(243,231,211,0) 100%);
  }
</style>
</head>
<body>
  <main class="label">
    <svg class="label__frame" viewBox="0 0 711 1200" aria-hidden="true">
      <!-- outer frame with notched corners -->
      <path d="M76 203 H635 V217 H649 V1134 H635 V1148 H76 V1134 H62 V217 H76 Z"
            fill="none" stroke="#fbf3e6" stroke-width="3"/>
      <!-- inner frame -->
      <rect x="73" y="214" width="565" height="923" fill="none" stroke="#fbf3e6" stroke-width="2"/>

      <!-- upper rules above title -->
      <line x1="95" y1="394" x2="616" y2="394" stroke="#fbf3e6" stroke-width="3" stroke-dasharray="60 6 18 5 40 7"/>
      <line x1="95" y1="404" x2="616" y2="404" stroke="#fbf3e6" stroke-width="2"/>

      <!-- side pointers beside title -->
      <polygon points="94,452 140,446 140,458" fill="#fbf3e6"/>
      <polygon points="617,452 571,446 571,458" fill="#fbf3e6"/>

      <!-- lower rules beneath title -->
      <line x1="95" y1="503" x2="616" y2="503" stroke="#fbf3e6" stroke-width="2"/>
      <line x1="95" y1="514" x2="616" y2="514" stroke="#fbf3e6" stroke-width="3" stroke-dasharray="40 7 18 5 60 6"/>
    </svg>

    <p class="brand-name">the Copper Comb</p>

    <h1 class="product-title">SHAMPOO</h1>

    <section class="ingredients">
      <p class="ingredients__heading">Ingredients:</p>
      <p>Insert information here as required, could also include product descrip&shy;tion or history/mock history of the brand.....</p>
    </section>

    <div class="moustache" role="img" aria-label="Curled handlebar moustache emblem in cream"></div>
  </main>
</body>
</html>
```